Bright Harbor Motors Business Card

Would like a cutting edge / high end Automotive Business card design. Please see current card which is old and dated. Would like to maintain the Bright Harbor Motors logo and same information (address, website, etc).

See our website for the look and feel of what we offer - www.brightharbormotors.example

Target Market(s)

Upper class car buyers

Contact Information for Business Card

Modern high end business card design

Requirements
Nice to have
• Carbon Fiber look background

```html
<!DOCTYPE html>
<html lang="en">
<head>
<meta charset="utf-8">
<title>Bright Harbor Motors Business Card</title>
<link href="https://fonts.googleapis.com/css2?family=Montserrat:wght@300;400;700&display=swap" rel="stylesheet">
<style>
  :root {
    --stage: #d3a516;
    --card-base: #0b0b0c;
    --card-mid: #17171a;
    --gold: #dcb556;
    --white: #f4f1ea;
    --glow-red: rgba(170, 36, 20, 0.55);
    --glow-amber: rgba(150, 90, 20, 0.45);
  }
  * { box-sizing: border-box; margin: 0; padding: 0; }
  html, body { width: 1200px; height: 900px; overflow: hidden; }
  body {
    background: var(--stage);
    font-family: "Montserrat", sans-serif;
    display: flex;
    flex-direction: column;
    align-items: center;
    justify-content: center;
    gap: 28px;
  }
  .card {
    position: relative;
    width: 600px;
    height: 343px;
    border-radius: 4px;
    overflow: hidden;
    box-shadow: 0 10px 24px rgba(0,0,0,0.35);
  }
  .card-texture {
    position: absolute;
    inset: 0;
    background:
      radial-gradient(ellipse 40% 35% at 100% 12%, var(--glow-red), transparent 70%),
      radial-gradient(ellipse 35% 30% at 0% 8%, var(--glow-amber), transparent 70%),
      linear-gradient(160deg, var(--card-mid) 0%, var(--card-base) 55%, #050506 100%);
  }
  .card-content { position: relative; height: 100%; }

  /* Front */
  .card-front .card-content {
    display: flex;
    flex-direction: column;
    align-items: center;
    justify-content: center;
    text-align: center;
  }
  .brand-name {
    font-weight: 700;
    color: var(--white);
    font-size: 34px;
    letter-spacing: 1px;
    text-transform: uppercase;
  }
  .brand-rule {
    width: 300px;
    height: 1px;
    background: var(--white);
    margin: 10px 0 12px;
  }
  .tagline {
    color: var(--white);
    font-weight: 300;
    font-size: 13px;
    letter-spacing: 0.5px;
  }
  .values {
    margin-top: 10px;
    background: var(--white);
    color: #111;
    font-size: 12px;
    font-weight: 400;
    padding: 2px 8px;
  }

  /* Back */
  .card-back .brand-block {
    position: absolute;
    top: 46px;
    right: 44px;
    text-align: right;
  }
  .card-back .brand-name { color: var(--gold); font-size: 32px; }
  .card-back .brand-rule { background: var(--gold); width: 100%; margin: 8px 0 0; }
  .address {
    position: absolute;
    top: 128px;
    right: 44px;
    color: var(--white);
    font-weight: 300;
    font-size: 14px;
    line-height: 1.4;
    text-align: right;
  }
  .person {
    position: absolute;
    left: 44px;
    bottom: 50px;
  }
  .person-name {
    color: var(--gold);
    font-weight: 700;
    font-size: 34px;
    line-height: 1.1;
  }
  .person-role {
    color: var(--white);
    font-weight: 300;
    font-size: 20px;
    margin-top: 4px;
  }
  .divider {
    position: absolute;
    left: 300px;
    bottom: 44px;
    width: 1px;
    height: 100px;
    background: rgba(220,181,86,0.45);
  }
  .contact-list {
    position: absolute;
    left: 322px;
    bottom: 46px;
    list-style: none;
    color: var(--white);
    font-weight: 300;
    font-size: 13px;
    line-height: 1;
  }
  .contact-list li {
    display: flex;
    align-items: center;
    gap: 10px;
    height: 24px;
  }
  .contact-icon { width: 13px; height: 13px; flex: none; }
</style>
</head>
<body>

  <section class="card card-front">
    <div class="card-texture" role="img" aria-label="Black carbon fiber weave texture with warm glows at the corners"></div>
    <div class="card-content">
      <div class="brand-name">Bright Harbor Motors</div>
      <div class="brand-rule"></div>
      <p class="tagline">Offering the Finest in Luxury &amp; Exotic Sport Cars</p>
      <p class="values">Quality | Integrity | Service</p>
    </div>
  </section>

  <section class="card card-back">
    <div class="card-texture" role="img" aria-label="Black carbon fiber weave texture with warm glows at the corners"></div>
    <div class="card-content">
      <div class="brand-block">
        <div class="brand-name">Bright Harbor Motors</div>
        <div class="brand-rule"></div>
      </div>
      <p class="address">1840 Harbor View Rd #B<br>Lakeside, CA 90210</p>

      <div class="person">
        <div class="person-name">Daniel Reyes</div>
        <div class="person-role">Owner</div>
      </div>

      <div class="divider"></div>

      <ul class="contact-list">
        <li>
          <svg class="contact-icon" viewBox="0 0 24 24" fill="var(--gold)"><path d="M6.6 10.8a15 15 0 0 0 6.6 6.6l2.2-2.2a1 1 0 0 1 1-.25 11.4 11.4 0 0 0 3.6.57 1 1 0 0 1 1 1V20a1 1 0 0 1-1 1A17 17 0 0 1 3 4a1 1 0 0 1 1-1h3.5a1 1 0 0 1 1 1c0 1.25.2 2.45.57 3.57a1 1 0 0 1-.25 1z"/></svg>
          555 014 2286
        </li>
        <li>
          <svg class="contact-icon" viewBox="0 0 24 24" fill="var(--gold)"><rect x="6" y="2" width="12" height="20" rx="2"/><rect x="8" y="4" width="8" height="13" fill="#111"/></svg>
          555 019 7731
        </li>
        <li>
          <svg class="contact-icon" viewBox="0 0 24 24" fill="none" stroke="var(--gold)" stroke-width="2.4"><circle cx="12" cy="12" r="4"/><path d="M16 8v5a3 3 0 0 0 6 0v-1a10 10 0 1 0-4 8"/></svg>
          daniel@brightharbormotors.example
        </li>
        <li>
          <svg class="contact-icon" viewBox="0 0 24 24" fill="none" stroke="var(--gold)" stroke-width="2"><circle cx="12" cy="12" r="10"/><path d="M2 12h20M12 2a15 15 0 0 1 0 20M12 2a15 15 0 0 0 0 20"/></svg>
          www.brightharbormotors.example
        </li>
      </ul>
    </div>
  </section>

</body>
</html>
```